Non-Profit, Organic, Natural Feel, Clean & Simple Business Cards

Looking for a business card design. Has an organic, natural, new-age, clean and simple look/feel. We are a non-profit group that works with Moringa(a health plant/superfood) by spreading and sharing seeds of Moringa. A design that stands out but clean and professional. I will upload our new logo design. The font can be changed. Also I will upload some pictures of Moringa.
Our Facebook page is www.socialvine.com/TavelliCircle Check us out to get a feel of us.

Target Market(s)

Everyone. Movers & Shakers of The Sustainable, Natural Medicines & Cosmetics, Organic Food Farming Industry. And To The Common Person Or A Local Family.

Industry/Entity Type

Sustainability

Contact Information for Business Card

Email: TavelliSoilCircle@Postvane.com
FB: www.Socialvine.com/TavelliCircle
Website: www.TavelliCircle.com

Requirements
Must have
• Image/Pic/Design of Moringa Leaves. Somewhere on the card. Clean and Clear. So you could easily identify the Moringa from the Business Card. Something Alive, Living, Green Feel to the card design.
Nice to have
• A warm, friendly, professional feel to the design. A organic sustainable concept/future with Moringa is the business card impression/image we are trying to present.

```html
<!DOCTYPE html>
<html lang="en">
<head>
<meta charset="utf-8">
<title>Tavelli Circle — Business Card</title>
<link rel="stylesheet" href="https://fonts.googleapis.com/css2?family=Open+Sans:wght@400;600;700&display=swap">
<style>
  :root {
    --stage: #000000;
    --card: #323335;
    --card-edge: #2a2b2d;
    --leaf-green: #6cc21f;
    --ink-light: #f2f2f2;
    --mark-grey: #a5a495;
    --divider: #2a2b2c;
  }
  * { margin: 0; padding: 0; box-sizing: border-box; }
  html, body {
    width: 1200px; height: 900px; overflow: hidden;
    background: var(--stage);
    font-family: "Open Sans", Arial, sans-serif;
  }
  .canvas { position: relative; width: 1200px; height: 900px; }
  .card {
    position: absolute; top: 271px;
    width: 456px; height: 281px;
    background: var(--card);
    border-radius: 12px;
    box-shadow: inset 0 0 0 1px var(--card-edge);
  }
  .card--front { left: 137px; }
  .card--back { left: 627px; }

  .brand-block {
    position: absolute; left: 30px; top: 70px;
    width: 140px; height: 167px;
    display: flex; flex-direction: column; align-items: center; justify-content: center;
  }
  .brand-dot {
    width: 14px; height: 14px; border-radius: 50%;
    background: var(--leaf-green); margin-bottom: 10px;
  }
  .brand-name {
    font-size: 15px; font-weight: 600; letter-spacing: 0.5px;
    color: var(--leaf-green); white-space: nowrap;
  }
  .divider {
    position: absolute; left: 187px; top: 74px;
    width: 1px; height: 136px; background: var(--divider);
  }
  .person { position: absolute; left: 219px; top: 72px; }
  .person-name {
    font-size: 16px; font-weight: 700; color: var(--leaf-green); line-height: 20px;
  }
  .person-role { font-size: 12.5px; color: var(--ink-light); line-height: 16px; }

  .contact-list {
    position: absolute; left: 219px; top: 135px; list-style: none;
  }
  .contact-item {
    display: flex; align-items: center; height: 19px;
    font-size: 12.5px; color: var(--ink-light); white-space: nowrap;
  }
  .contact-icon { width: 12px; height: 12px; margin-right: 8px; flex: none; }

  .back-mark {
    position: absolute; left: 0; right: 0; top: 117px;
    display: flex; align-items: center; justify-content: center;
  }
  .back-dot {
    width: 16px; height: 16px; border-radius: 50%;
    background: var(--leaf-green); margin-right: 14px;
  }
  .back-name {
    color: var(--mark-grey); font-weight: 400; font-size: 34px;
    letter-spacing: 2px; line-height: 1; white-space: nowrap;
  }
</style>
</head>
<body>
<main class="canvas">
  <section class="card card--front" aria-label="Business card front">
    <div class="brand-block">
      <div class="brand-dot"></div>
      <span class="brand-name">Tavelli Circle</span>
    </div>
    <div class="divider"></div>
    <div class="person">
      <p class="person-name">Marcus Ellery</p>
      <p class="person-role">Managing Director</p>
    </div>
    <ul class="contact-list">
      <li class="contact-item">
        <svg class="contact-icon" viewBox="0 0 12 12" aria-hidden="true"><path fill="#6cc21f" d="M2.3 1.2l1.8 1.9-.9 1.3c.8 1.5 1.9 2.6 3.4 3.4l1.3-.9 1.9 1.8-1 1.8C5.2 10.3 1.7 6.8 1.5 2.2z"/></svg>
        (044)-318-2260
      </li>
      <li class="contact-item">
        <svg class="contact-icon" viewBox="0 0 12 12" aria-hidden="true"><rect x="1" y="2.5" width="10" height="7" fill="#6cc21f"/><path d="M1 2.5l5 4 5-4" fill="none" stroke="#323335" stroke-width="1"/></svg>
        TavelliSoilCircle@Postvane.com
      </li>
      <li class="contact-item">
        <svg class="contact-icon" viewBox="0 0 12 12" aria-hidden="true"><circle cx="6" cy="6" r="5" fill="#6cc21f"/><path d="M1 6h10M6 1c-2.2 2.8-2.2 7.2 0 10M6 1c2.2 2.8 2.2 7.2 0 10" fill="none" stroke="#323335" stroke-width=".8"/></svg>
        www.TavelliCircle.com
      </li>
      <li class="contact-item">
        <svg class="contact-icon" viewBox="0 0 12 12" aria-hidden="true"><circle cx="6" cy="6" r="3" fill="#6cc21f"/></svg>
        TavelliCircle
      </li>
    </ul>
  </section>

  <section class="card card--back" aria-label="Business card back">
    <div class="back-mark">
      <div class="back-dot"></div>
      <p class="back-name">Tavelli Circle</p>
    </div>
  </section>
</main>
</body>
</html>
```